Maple Cove Laser Dermal Studio needs an 8 page WP redesign

We need a colorful re-design for an 8 page Wordpress website. The current preliminary website is live. The home page URL is http://maplecovelaserdermalstudio.com The new logo is live on the website also. I would like a (re)design using the colors that are represented by the new logo file, and any additional complimentary colors. The information regarding the business can be found on the website already, so please review it for insight. The name of the business is "Maple Cove Laser Dermal Studio".

Target Market(s)

The targeted website viewer is an adult female between the ages of 30 and 75 who is interested in facial renewal, wart removal and scar removal. This website should inspire in the target viewer the benefits of laser facial renewal, wart removal and new scar removal. Potential website viewers are wanting and searching for improved skin health and appearance. The website must represent the essence of a professional spa business.

Industry/Entity Type

Business

Font styles to use
Sans Serif

Requirements
Must have
• - The phone number placed in a visible and high value widget area that allows mobile phone browser dialing.

```html
<!DOCTYPE html>
<html lang="en">
<head>
<meta charset="utf-8">
<title>Maple Cove Laser Dermal Studio</title>
<link rel="stylesheet" href="https://fonts.googleapis.com/css2?family=Open+Sans:wght@400;600;700&family=Oswald:wght@300;500&family=Noto+Serif&display=swap">
<style>
:root{
  --purple:#a51bb0;
  --purple-deep:#8e1499;
  --plum:#2f1a2e;
  --plum-mid:#4a2a45;
  --ink:#1d1d24;
  --text:#555;
  --white:#fff;
  --sky:#d7ecfb;
  --sky-deep:#48c4f3;
}
*{margin:0;padding:0;box-sizing:border-box}
html,body{width:1200px;height:2314px;overflow:hidden;background:var(--white)}
body{position:relative;font-family:"Open Sans",Arial,sans-serif;color:var(--text)}
.abs{position:absolute}
a{color:inherit;text-decoration:none}

/* hero */
.hero{left:0;top:0;width:1200px;height:663px;overflow:hidden;
  background:linear-gradient(100deg,var(--sky-deep) 0%,#9fdcfa 18%,var(--sky) 45%,#eef6fd 70%,#dfe9fb 100%)}
.hero-photo{left:560px;top:175px;width:500px;height:488px;border-radius:48% 48% 0 0/40% 40% 0 0;
  background:radial-gradient(ellipse at 55% 40%,#f6dccf 0%,#edc9b7 45%,rgba(237,201,183,0) 72%)}
.brand{left:0;top:38px;width:1200px;text-align:center;font-size:40px;font-weight:700;color:var(--purple);letter-spacing:-.5px}
.nav{left:151px;top:130px;width:896px;height:44px;background:var(--purple);display:flex;justify-content:space-between;
  font-family:"Noto Serif",Georgia,serif;font-size:13.5px;color:var(--white);text-transform:uppercase;white-space:nowrap}
.nav a{display:flex;align-items:center;padding:0 13px}
.nav a.active{background:#3a1433;padding:0 16px}
.hero-kicker{left:151px;top:296px;font-family:Oswald,sans-serif;font-weight:300;font-size:27px;line-height:36px;color:var(--ink)}
.hero-title{left:151px;top:338px;font-family:Oswald,sans-serif;font-weight:500;font-size:48px;line-height:60px;color:var(--ink);letter-spacing:.5px}
.hero-copy{left:152px;top:406px;width:420px;font-size:13.5px;line-height:21px;color:#333}
.hero-next{left:152px;top:488px;width:46px;height:46px}

/* contact band */
.band{left:0;top:663px;width:1200px;height:74px;background:var(--purple);color:var(--white)}
.band-lead{left:151px;top:27px;font-size:14px}
.band-item{top:13px;display:flex;align-items:center;gap:12px}
.band-item svg{width:44px;height:44px}
.band-item b{display:block;font-size:16px;font-weight:600}
.band-item span{font-size:14px}

/* about */
.about-title{left:152px;top:767px;font-size:18.5px;font-weight:700;color:var(--purple)}
.rule{height:2px;background:var(--purple)}
.about-copy{left:154px;top:818px;width:585px;font-size:11.4px;line-height:21.6px;color:#444}
.about-photo{left:760px;top:787px;width:290px;height:270px;
  background:linear-gradient(160deg,#f4e7e1 0%,#e8d1c6 45%,#f7f7f7 100%);border-radius:30px 60px 10px 40px}
.round-btn{width:32px;height:32px}

/* testimonials */
.testi{left:0;top:1092px;width:1200px;height:247px;background:linear-gradient(180deg,#3b2235,var(--plum) 60%,#4a2b44)}
.testi-title{left:0;top:33px;width:1200px;text-align:center;color:var(--white);font-size:18px;font-weight:600}
.testi-avatar{left:154px;top:75px;width:118px;height:118px;border-radius:50%;border:4px solid var(--white);
  background:linear-gradient(160deg,#9b7e6e,#d9bfae)}
.testi-quote{left:299px;top:83px;width:740px;color:var(--white);font-size:13px;line-height:22.5px}
.testi-name{left:299px;top:168px;color:var(--white);font-size:15.5px;font-weight:600}
.dots{left:578px;top:205px;display:flex;gap:8px}
.dots i{width:7px;height:7px;border-radius:50%;background:#9b8b99}
.dots i:first-child{background:var(--white)}

/* gallery strip */
.strip{top:1339px;height:227px}
.strip-feature{left:62px;width:359px;background:linear-gradient(135deg,#b62dc2,#a51bb0 60%,#c04ccb);
  color:var(--white);display:flex;align-items:center;justify-content:center;font-size:17px;font-weight:700}

/* blog */
.blog-title{left:0;top:1594px;width:1200px;text-align:center;font-size:18px;font-weight:600;color:var(--purple)}
.card{top:1653px;width:282px;height:200px}
.card-date{left:0;top:0;width:46px;height:59px;background:var(--purple);color:var(--white);text-align:center;
  font-size:12px;line-height:14.5px;padding-top:7px}
.card-img{left:46px;top:0;width:236px;height:152px}
.card-meta{left:8px;top:70px;width:30px;text-align:center;font-size:9px;color:#888}
.card-meta svg{display:block;margin:0 auto}
.card-copy{left:46px;top:158px;width:236px;font-size:12.5px;line-height:19px;color:#666}
.view-all{left:947px;top:1871px;width:100px;text-align:right;font-size:11px;font-weight:600;color:var(--purple)}

/* promo */
.promo{left:151px;top:1919px;width:896px;height:291px;background:var(--plum);color:var(--white);overflow:hidden}
.promo-lead{left:26px;top:30px;font-size:17px;font-weight:600}
.promo-line{height:1px;background:#6d5069}
.ribbon{left:26px;top:86px;width:301px;height:40px}
.ribbon span{position:absolute;left:16px;top:8px;font-family:Oswald,sans-serif;font-size:17px;letter-spacing:.3px}
.promo-copy{left:26px;top:147px;width:360px;font-size:13px;line-height:19.5px;font-weight:600}
.deal{top:220px;display:flex;align-items:center;gap:10px}
.deal-text{font-size:14px;line-height:17px;text-align:center}
.deal-sep{top:225px;width:1px;height:52px;background:#6d5069}
.hurry{left:436px;top:26px;width:200px;text-align:center;font-size:16px;font-weight:700}
.special{left:406px;top:137px;width:260px;text-align:center;font-size:15.5px;line-height:22px;font-weight:700}
.promo-photo{left:660px;top:0;width:236px;height:291px;
  background:radial-gradient(ellipse at 55% 45%,#f0d2c0 0%,#d8ab94 40%,rgba(47,26,46,0) 72%)}

/* footer */
.footer{left:0;top:2246px;width:1200px;height:68px;background:var(--purple);color:var(--white)}
.footer-links{left:151px;top:17px;font-size:11.5px}
.footer-copy{left:151px;top:37px;font-size:11.5px}
.social{left:900px;top:17px;display:flex;gap:5px}
.social i{width:34px;height:34px;border-radius:50%;border:2px solid #d681dd;background:#b53ac0}
</style>
</head>
<body>

<header class="abs hero">
  <div class="abs hero-photo" role="img" aria-label="Smiling blonde woman touching her cheek, bare-shouldered, palm held open"></div>
  <div class="abs brand">Maple Cove Laser Dermal Studio</div>
  <nav class="abs nav">
    <a class="active" href="#">Home</a><a href="#">About Us</a><a href="#">Skin Renewal</a><a href="#">Scar Removal</a><a href="#">Wart Removal</a><a href="#">Your Visit</a><a href="#">Blog</a><a href="#">Contact Us</a>
  </nav>
  <p class="abs hero-kicker">FOR BEAUTY SKIN LASER TREATMENTS</p>
  <h1 class="abs hero-title">SKIN REJUVENATION</h1>
  <p class="abs hero-copy">Lorem ipsum dolor sit amet consectetur adipiscing elit oneciacul bibendum ellentesque efficitur...</p>
  <svg class="abs hero-next" viewBox="0 0 46 46"><circle cx="23" cy="23" r="21.5" fill="none" stroke="#fff" stroke-width="2"/><path d="M20 16l7 7-7 7" fill="none" stroke="#fff" stroke-width="2.5"/></svg>
</header>

<section class="abs band">
  <p class="abs band-lead">READY FOR HEALTHY SKIN AND BODY?</p>
  <a class="abs band-item" style="left:482px" href="tel:2815550147">
    <svg viewBox="0 0 44 44"><circle cx="22" cy="22" r="20.5" fill="none" stroke="#fff" stroke-width="2"/><path d="M16 13c1.5-1 3 0 3.5 1.5l1 3c.3 1-.5 1.8-1.3 2.3 1 2.4 2.7 4.2 5 5.3.5-.8 1.3-1.6 2.3-1.3l3 1c1.5.5 2.5 2 1.5 3.5-1.5 2.3-4 2.6-6.5 1.3-4-2-7-5-9-9-1.3-2.6-1-5.2.5-7.6z" fill="#fff"/></svg>
    <div><b>Call for Appointment</b><span>281-555-0147</span></div>
  </a>
  <a class="abs band-item" style="left:738px" href="mailto:info@maplecovelaserdermalstudio.com">
    <svg viewBox="0 0 44 44"><circle cx="22" cy="22" r="20.5" fill="none" stroke="#fff" stroke-width="2"/><path d="M13 19l9-6 9 6v11H13z" fill="#fff"/><path d="M13 19l9 6 9-6" fill="none" stroke="#a51bb0" stroke-width="1.5"/></svg>
    <div><b>Email Us</b><span>info@maplecovelaserdermalstudio.com</span></div>
  </a>
</section>

<section>
  <div class="abs about-photo" role="img" aria-label="Woman wrapped in a white towel sitting with knees drawn up"></div>
  <h2 class="abs about-title">HAVE YOU CONSIDERED LASER SKIN RENEWAL THERAPY?</h2>
  <div class="abs rule" style="left:152px;top:804px;width:146px"></div>
  <p class="abs about-copy">You will truly love laser skin renewal if your skin is showing signs of premature aging or the skin has sustained sun damage. Conditions such as excessive redness due to sun exposure or fine lines will be concerns of the past. In fact, laser skin therapy is a unique and innovative way to enjoy youthful and healthy skin without resorting to painful and inconvenient surgery. Both men and women are receiving benefits from laser skin therapy.<br>The literature contains ample scientific evidence to support laser skin renewal. After this therapy, your skin will produce collagen, which reduces and minimizes the appearance of fine lines and wrinkles. Imagine getting all this with minimal pain and no downtime? Doesn't it make you feel like getting in touch with our laser skin specialist today?</p>
  <svg class="abs round-btn" style="left:153px;top:1024px" viewBox="0 0 32 32"><circle cx="16" cy="16" r="16" fill="#a51bb0"/><path d="M10 16h11M17 11l5 5-5 5" fill="none" stroke="#fff" stroke-width="2.5"/></svg>
</section>

<section class="abs testi">
  <h2 class="abs testi-title">TESTIMONIALS</h2>
  <div class="abs rule" style="left:526px;top:68px;width:148px;background:#fff"></div>
  <div class="abs testi-avatar" role="img" aria-label="Portrait of a client wearing glasses"></div>
  <p class="abs testi-quote">&ldquo; Lorem ipsum dolor sit amet, consectetur adipiscing elit. Maecenas nunc ex, dictum nec ipsum vel, vulputate luctus nisl. Nunc nec metus cursus, dignissim nunc sed, porta urna. Pellentesque scelerisque seullamcor rhoncus. Cras volutpat turpis vel sem pharetra, at pellentesque metus ullamcorper. &rdquo;</p>
  <p class="abs testi-name">Mark Lorem ispum</p>
  <div class="abs dots"><i></i><i></i><i></i></div>
</section>

<section>
  <div class="abs strip" style="left:0;width:62px;background:linear-gradient(120deg,#c9a28c,#7b5a48)" role="img" aria-label="Hands giving a stone massage"></div>
  <div class="abs strip strip-feature">SKIN CARE LASER TERATMENTS</div>
  <div class="abs strip" style="left:421px;width:358px;background:linear-gradient(120deg,#d8d8d3,#b9a196 50%,#e6e4de)" role="img" aria-label="Dark-haired woman with a flower in her hair"></div>
  <div class="abs strip" style="left:779px;width:358px;background:linear-gradient(90deg,#a7a7a9,#d6b8a6 55%,#bdbdbf)" role="img" aria-label="Smiling woman with hair in a bun"></div>
  <div class="abs strip" style="left:1137px;width:63px;background:linear-gradient(90deg,#d9dbe6,#b7bccf)" role="img" aria-label="Soft spa scene"></div>
</section>

<section>
  <h2 class="abs blog-title">LATEST BLOG</h2>
  <div class="abs rule" style="left:535px;top:1632px;width:130px"></div>

  <article class="abs card" style="left:151px">
    <div class="abs card-date">01<br>JAN<br>2015</div>
    <div class="abs card-img" style="background:linear-gradient(90deg,#4bb6d6,#d7a584 55%,#8a5d43)" role="img" aria-label="Smiling woman at the beach"></div>
    <div class="abs card-meta"><svg width="26" height="24" viewBox="0 0 26 24"><rect x="2" y="2" width="22" height="15" rx="2" fill="none" stroke="#999" stroke-width="1.5"/><path d="M8 17l-2 5 6-5" fill="none" stroke="#999" stroke-width="1.5"/><path d="M13 6v7M9.5 9.5h7" stroke="#999" stroke-width="1.5"/></svg><svg width="22" height="20" viewBox="0 0 22 20" style="margin-top:10px"><path d="M11 18S2 12 2 6.5A4.5 4.5 0 0 1 11 5a4.5 4.5 0 0 1 9 1.5C20 12 11 18 11 18z" fill="none" stroke="#999" stroke-width="1.5"/></svg>19</div>
    <p class="abs card-copy">Lorem ipsum dolor amet, consectedi Fusce dictum consectetur erat.</p>
  </article>

  <article class="abs card" style="left:459px">
    <div class="abs card-date">2<br>JAN<br>2015</div>
    <div class="abs card-img" style="background:linear-gradient(90deg,#7a6a5d,#c49077 50%,#6d5d52)" role="img" aria-label="Young woman with dark hair against wooden wall"></div>
    <div class="abs card-meta"><svg width="26" height="24" viewBox="0 0 26 24"><rect x="2" y="2" width="22" height="15" rx="2" fill="none" stroke="#999" stroke-width="1.5"/><path d="M8 17l-2 5 6-5" fill="none" stroke="#999" stroke-width="1.5"/><path d="M13 6v7M9.5 9.5h7" stroke="#999" stroke-width="1.5"/></svg><svg width="22" height="20" viewBox="0 0 22 20" style="margin-top:10px"><path d="M11 18S2 12 2 6.5A4.5 4.5 0 0 1 11 5a4.5 4.5 0 0 1 9 1.5C20 12 11 18 11 18z" fill="none" stroke="#999" stroke-width="1.5"/></svg>19</div>
    <p class="abs card-copy">Lorem ipsum dolor amet, consectedi lo Fusce dictum consectetur erat.</p>
  </article>

  <article class="abs card" style="left:766px">
    <div class="abs card-date">2<br>JAN<br>2015</div>
    <div class="abs card-img" style="background:linear-gradient(90deg,#5fa9cf,#dfe7ef 45%,#7fb3d3)" role="img" aria-label="Woman in winter frost styling"></div>
    <div class="abs card-meta"><svg width="26" height="24" viewBox="0 0 26 24"><rect x="2" y="2" width="22" height="15" rx="2" fill="none" stroke="#999" stroke-width="1.5"/><path d="M8 17l-2 5 6-5" fill="none" stroke="#999" stroke-width="1.5"/><path d="M13 6v7M9.5 9.5h7" stroke="#999" stroke-width="1.5"/></svg><svg width="22" height="20" viewBox="0 0 22 20" style="margin-top:10px"><path d="M11 18S2 12 2 6.5A4.5 4.5 0 0 1 11 5a4.5 4.5 0 0 1 9 1.5C20 12 11 18 11 18z" fill="none" stroke="#999" stroke-width="1.5"/></svg>19</div>
    <p class="abs card-copy">Lorem ipsum dolor amet, consectedi lo Fusce dictum consectetur erat.</p>
  </article>

  <a class="abs view-all" href="#">VIEW ALL</a>
</section>

<section class="abs promo">
  <div class="abs promo-photo" role="img" aria-label="Smiling woman with hair in a bun, bare-shouldered"></div>
  <p class="abs promo-lead">Restore your youthful skin this year!</p>
  <div class="abs promo-line" style="left:26px;top:68px;width:330px"></div>
  <div class="abs ribbon">
    <svg width="301" height="40" viewBox="0 0 301 40" style="position:absolute;left:0;top:0"><path d="M0 0h301l-16 20 16 20H0z" fill="#a51bb0"/></svg>
    <span>NEW YEARS RESOLUTION SPECIAL!</span>
  </div>
  <div class="abs promo-line" style="left:26px;top:135px;width:330px"></div>
  <p class="abs promo-copy">Take advantage of our laser skin renewal specials for single or multiple sessions at low pricing.</p>

  <div class="abs deal" style="left:26px">
    <svg width="56" height="56" viewBox="0 0 56 56"><polygon points="28,0 33,9 43,4 43,15 54,16 48,25 56,33 45,37 48,48 37,46 33,56 28,48 23,56 19,46 8,48 11,37 0,33 8,25 2,16 13,15 13,4 23,9" fill="#a51bb0"/><text x="28" y="35" text-anchor="middle" font-family="Open Sans,sans-serif" font-weight="700" font-size="20" fill="#fff">1</text></svg>
    <div class="deal-text">Single Session<br>Deal - $199</div>
  </div>
  <div class="abs deal-sep" style="left:200px"></div>
  <div class="abs deal" style="left:238px">
    <svg width="56" height="56" viewBox="0 0 56 56"><polygon points="28,0 33,9 43,4 43,15 54,16 48,25 56,33 45,37 48,48 37,46 33,56 28,48 23,56 19,46 8,48 11,37 0,33 8,25 2,16 13,15 13,4 23,9" fill="#a51bb0"/><text x="28" y="35" text-anchor="middle" font-family="Open Sans,sans-serif" font-weight="700" font-size="20" fill="#fff">3</text></svg>
    <div class="deal-text">Single Session<br>Deal - $459</div>
  </div>
  <div class="abs deal-sep" style="left:413px"></div>
  <div class="abs deal" style="left:449px">
    <svg width="56" height="56" viewBox="0 0 56 56"><polygon points="28,0 33,9 43,4 43,15 54,16 48,25 56,33 45,37 48,48 37,46 33,56 28,48 23,56 19,46 8,48 11,37 0,33 8,25 2,16 13,15 13,4 23,9" fill="#a51bb0"/><text x="28" y="35" text-anchor="middle" font-family="Open Sans,sans-serif" font-weight="700" font-size="20" fill="#fff">6</text></svg>
    <div class="deal-text">Single Session<br>Deal - $899</div>
  </div>

  <p class="abs hurry">HUURY UP</p>
  <svg class="abs" style="left:497px;top:55px" width="78" height="70" viewBox="0 0 78 70"><polygon points="39,2 47,12 60,8 61,21 75,26 66,36 73,48 59,51 55,64 42,58 30,67 25,54 11,53 14,40 3,31 15,24 15,11 29,13" fill="#c8202a"/></svg>
  <p class="abs special">Special ENDS January<br>3, 2015 at 5:00 PM.</p>
</section>

<footer class="abs footer">
  <p class="abs footer-links">Home &nbsp;/&nbsp; About Us &nbsp;/&nbsp; Skin Renewal &nbsp;/&nbsp; Scar Removal &nbsp;/&nbsp; Wart Removal &nbsp;/&nbsp; Your Visit &nbsp;/&nbsp; Blog &nbsp;/&nbsp; Contact</p>
  <p class="abs footer-copy">Copyright &nbsp;2015 Maple Cove Laser Dermal Studio. All right reserved.</p>
  <div class="abs social"><i></i><i></i><i></i><i></i></div>
</footer>

</body>
</html>
```